A4 Single Page Brochure for Private Cloud Offerings

Theme: Futuristic Tech Company

Brightmoor Systems is looking to offer private cloud services for our enterprise customers in Perth-based data-centres that provides our clients with a lower-cost alternative to Nimbra or KLT yielding better performance.

We are looking for a single A4 brochure with a great graphics design theme to promote these services.

We will be providing five tiers:
- Starter
- Growth
- Professional
- Premier
- Elite

Each plan must list on the brochure the Max VMs, CPU cores, Memory and SSD storage allocated. Refer to the uploaded PNG file.

The brochure must list the following selling points:

- Hosted in a local Perth-based TIER3 and TIER4 datacentres
- WA owned hosting - support local
- Low latency - ultra fast local hosting
- Includes Quorra Host Datacentre licensing
- Includes WallHaven Managed Firewalls for Enterprise level threat detection
- Includes all infrastructure maintenance services
- Full self management of VMs through customer portal
- Includes a 1gbps Internet link
- Predictable fixed monthly fee with no dynamic billing
- No additional charges for Storage Transactions, Internet Usage, VM Snapshots, Datacentre Bandwidth Usage and Firewall Traffic Usage.
- Highly available cluster, no single point of failure.
- Pricing is based on 36 months commit
- Yearly rate increases capped to a maximum of Australian CPI
- All plans have 24/7/365 support with dedicated after hours number.
- Managed backup and managed disaster recovery services can be added to plans

Service provided in accordance with our terms and conditions.

We need the ability to EDIT the brochure to adjust pricing after we receive the final project.

Please do not utilise "Pushing the Boundaries of Technology" - our brand is being replaced with "Specialised Consulting". New website is under development but not launched yet.

Target Market(s)

Information Technology Sector

Colors
0054AA
0677BA
7BADD7
CADEEF
E8F1F8

Requirements
Must have
• Theme of Brightmoor is Blue
Should not have
• Extremely stock imagary that just looks "cheap and stock"

```html
<!DOCTYPE html>
<html lang="en">
<head>
<meta charset="utf-8">
<title>Brightmoor Private Cloud Plans</title>
<link href="https://fonts.googleapis.com/css2?family=Lato:wght@400;700;900&display=swap" rel="stylesheet">
<style>
  :root{
    --stage:#808080;
    --navy:#1410a3;
    --navy-deep:#0b0e96;
    --sky:#7cc3ef;
    --sky-pale:#d4f0fb;
    --ink:#1b1b2a;
    --band:#8ccff4;
    --white:#ffffff;
    --photo-mid:#5f86bd;
    --photo-dark:#0e2a5c;
    --skyline:#a9d8f5;
  }
  *{margin:0;padding:0;box-sizing:border-box}
  html,body{width:1200px;height:1000px;overflow:hidden}
  body{background:var(--stage);font-family:"Lato",sans-serif;color:var(--ink)}
  .brochure{position:absolute;left:302px;top:79px;width:595px;height:842px;overflow:hidden;
    background:linear-gradient(180deg,var(--sky-pale) 0%,#eef9fd 30%,var(--white) 50%)}
  .brand{position:absolute;left:25px;top:36px;display:flex;align-items:center;gap:8px}
  .brand-mark{width:22px;height:22px;background:var(--navy)}
  .brand-name{font-weight:900;font-size:17px;letter-spacing:1px;color:var(--navy)}
  .skyline{position:absolute;left:277px;top:12px;width:267px;height:89px;
    background:linear-gradient(180deg,rgba(169,216,245,0) 0%,var(--skyline) 60%,var(--skyline) 100%)}
  .hero-photo{position:absolute;left:0;top:178px;width:595px;height:417px;
    background:linear-gradient(180deg,rgba(255,255,255,0) 0%,#b8c9de 22%,var(--photo-mid) 45%,#2a4f8a 70%,var(--photo-dark) 100%)}
  .hero-rule{position:absolute;left:0;top:595px;width:595px;height:6px;
    background:linear-gradient(180deg,#000 0%,#1a2a55 100%)}
  .plans-card{position:absolute;left:30px;top:101px;width:536px;height:285px;background:var(--white);
    border-radius:17px;overflow:hidden;box-shadow:0 4px 14px rgba(20,40,90,.18)}
  .plans-title{position:absolute;top:12px;width:100%;text-align:center;font-weight:900;font-size:14px;
    letter-spacing:.6px;color:var(--navy);word-spacing:3px}
  .plans-head{position:absolute;top:38px;left:0;width:100%;height:37px;
    background:linear-gradient(90deg,var(--sky) 0%,#5d8fe0 50%,var(--navy-deep) 100%)}
  .plans-row{position:absolute;left:0;width:100%;height:34px;border-bottom:1px solid #eef2f6}
  .plans-row.cost{height:41px;background:linear-gradient(90deg,#d7f0fc 0%,var(--band) 100%);border:0}
  .cell{position:absolute;top:50%;transform:translate(-50%,-50%);font-weight:700;font-size:12px;white-space:nowrap}
  .plans-head .cell{color:var(--white);font-size:12px}
  .row-label{position:absolute;left:23px;top:50%;transform:translateY(-50%);font-weight:900;font-size:12px;color:var(--navy)}
  .cost .row-label{color:var(--ink);font-weight:700}
  .cost .cell{font-weight:900;color:var(--ink)}
  .c1{left:173px}.c2{left:250px}.c3{left:331px}.c4{left:408px}.c5{left:483px}
  .plans-note{position:absolute;left:24px;top:266px;font-size:8px;font-weight:900;color:var(--navy)}
  .features{position:absolute;left:0;top:601px;width:595px;height:219px;
    background:linear-gradient(180deg,#c9eef9 0%,#e9f7fc 50%,var(--white) 100%)}
  .features-divider{position:absolute;left:297px;top:2px;width:1px;height:200px;background:var(--ink)}
  .feature{position:absolute;font-size:10px;line-height:12px;font-weight:700;color:#1f2430;padding-left:15px}
  .feature::before{content:"";position:absolute;left:1px;top:2px;width:5px;height:5px;
    border-right:2.4px solid var(--navy);border-top:2.4px solid var(--navy);transform:rotate(45deg)}
  .col-left .feature{left:23px;width:255px}
  .col-right .feature{left:322px;width:260px}
  .footer-band{position:absolute;left:0;top:820px;width:595px;height:22px;background:var(--navy-deep);
    color:var(--white);font-size:6.5px;padding:6px 24px}
</style>
</head>
<body>
<main class="brochure">
  <header class="brand">
    <span class="brand-mark"></span>
    <span class="brand-name">BRIGHTMOOR</span>
  </header>
  <div class="skyline" role="img" aria-label="Pale blue Perth city skyline silhouette"></div>
  <div class="hero-photo" role="img" aria-label="Hands typing on a laptop with glowing cyber-security icons overlay in blue tones"></div>
  <div class="hero-rule"></div>

  <section class="plans-card">
    <h1 class="plans-title">BRIGHTMOOR PRIVATE CLOUD PLANS</h1>
    <div class="plans-head">
      <span class="cell c1">Starter</span><span class="cell c2">Growth</span><span class="cell c3">Professional</span><span class="cell c4">Premier</span><span class="cell c5">Elite</span>
    </div>
    <div class="plans-row" style="top:80px">
      <span class="row-label">Max VMs</span>
      <span class="cell c1">5</span><span class="cell c2">10</span><span class="cell c3">15</span><span class="cell c4">20</span><span class="cell c5">25</span>
    </div>
    <div class="plans-row" style="top:114px">
      <span class="row-label">CPU cores</span>
      <span class="cell c1">8</span><span class="cell c2">16</span><span class="cell c3">32</span><span class="cell c4">48</span><span class="cell c5">64</span>
    </div>
    <div class="plans-row" style="top:150px">
      <span class="row-label">Memory (GB)</span>
      <span class="cell c1">64</span><span class="cell c2">128</span><span class="cell c3">192</span><span class="cell c4">256</span><span class="cell c5">320</span>
    </div>
    <div class="plans-row" style="top:185px">
      <span class="row-label">Storage SSD (TB)</span>
      <span class="cell c1">3</span><span class="cell c2">8</span><span class="cell c3">15</span><span class="cell c4">20</span><span class="cell c5">30</span>
    </div>
    <div class="plans-row cost" style="top:219px">
      <span class="row-label">Monthly Cost</span>
      <span class="cell c1">$1028.01</span><span class="cell c2">$3426.64</span><span class="cell c3">$4626.05</span><span class="cell c4">$5482.72</span><span class="cell c5">$7196.07</span>
    </div>
    <p class="plans-note">For larger plan, ask us.</p>
  </section>

  <section class="features">
    <div class="features-divider"></div>
    <div class="col-left">
      <p class="feature" style="top:22px">Hosted in a local Perth-based TIER3 and TIER4 datacentres</p>
      <p class="feature" style="top:53px">WA owned hosting - support local</p>
      <p class="feature" style="top:74px">Low latency - ultra fast local hosting</p>
      <p class="feature" style="top:95px">Includes Quorra Host Datacentre licensing</p>
      <p class="feature" style="top:116px">Includes WallHaven Managed Firewalls for Enterprise level threat detection</p>
      <p class="feature" style="top:147px">Includes all infrastructure maintenance services</p>
      <p class="feature" style="top:167px">Full self management of VMs through customer portal</p>
      <p class="feature" style="top:188px">Includes a 1gbps Internet link</p>
    </div>
    <div class="col-right">
      <p class="feature" style="top:22px">Predictable fixed monthly fee with no dynamic billing</p>
      <p class="feature" style="top:46px">No additional charges for Storage Transactions, Internet Usage, VM Snapshots, Datacentre Bandwidth Usage and Firewall Traffic Usage.</p>
      <p class="feature" style="top:95px">Highly available cluster, no single point of failure.</p>
      <p class="feature" style="top:119px">Pricing is based on 36 months commit</p>
      <p class="feature" style="top:143px">All plans have 24/7/365 support with dedicated after hours number.</p>
      <p class="feature" style="top:177px">Managed backup and managed disaster recovery services can be added to plans</p>
    </div>
  </section>

  <footer class="footer-band">Service provided in accordance with our terms and conditions.</footer>
</main>
</body>
</html>
```